Corbell Estates LLC stationary for a real estate property management company.

Create stationary (letterhead, envelopes, business cards) using Corbell Estates LLC logo as primary creative element. Stationary design needs to be horizontal, leaving as much space as possible for correspondence copy. See attached Creative Brief and past stationary files for details.

Target Market(s)

Prospective apartment residents and current residents, vendors, and government agencies.

Industry/Entity Type

Property Management

Contact Information for Business Card

Business card employee title: Property Manager. Should include address, phone, fax, email, website, slogan, and Corbell Estates logo.

Font styles to use
Sans Serif

Colors
0592cd
000000

Requirements
Must have
• Tone should be conservative, institutional, business (i.e. banking, finance, real estate). Must include: address, phone, fax, website, and slogan (see attached Creative Brief). Should be a horizontal design, leaving as much room as possible for letter correspondence copy.
Nice to have
• Please use an Arial or Helvetica style font.
Should not have
• Letterhead layout should leave as much room as possible for copy.

```html
<!DOCTYPE html>
<html lang="en">
<head>
<meta charset="utf-8">
<title>Corbell Estates LLC – Stationery</title>
<link href="https://fonts.googleapis.com/css2?family=Arimo:wght@400;700&family=PT+Sans:wght@400&display=swap" rel="stylesheet">
<style>
  :root {
    --brand-blue: #0592cd;
    --ink: #000000;
    --text-grey: #555;
    --paper: #f6f6f6;
    --canvas-bg: #e4e4e4;
    --faint: #d9e9f2;
    --line: #d0d6dc;
  }
  * { margin: 0; padding: 0; box-sizing: border-box; }
  html, body { width: 1200px; height: 754px; overflow: hidden; }
  body { background: var(--canvas-bg); font-family: "Arimo", Arial, sans-serif; position: relative; }

  .sheet { position: absolute; background: var(--paper); box-shadow: 0 1px 4px rgba(0,0,0,.18); }

  .brand { display: flex; align-items: center; gap: 6px; color: var(--brand-blue); font-weight: 700; white-space: nowrap; }
  .brand-square { background: var(--brand-blue); flex: none; }
  .slogan { color: var(--brand-blue); font-weight: 400; white-space: nowrap; }

  /* Letterhead */
  .letterhead { left: 36px; top: 32px; width: 490px; height: 690px; }
  .letterhead .brand { position: absolute; left: 0; top: 32px; font-size: 15px; }
  .letterhead .brand-square { width: 34px; height: 34px; }
  .letterhead-contact { position: absolute; right: 40px; top: 53px; text-align: right; font-size: 8px; line-height: 11.5px; color: var(--text-grey); }
  .letterhead .slogan { position: absolute; left: 40px; top: 70px; font-size: 8px; }
  .letter-body { position: absolute; left: 30px; top: 193px; width: 427px; font-family: "PT Sans", sans-serif; color: #333; }
  .letter-body .greeting { font-size: 13px; line-height: 16px; margin-bottom: 28px; text-align: left; }
  .letter-body p { font-size: 7.2px; line-height: 11.8px; margin-bottom: 11.5px; text-align: justify; }
  .letter-body .closing { margin-top: 22px; }
  .signature { width: 64px; height: 28px; margin-top: 10px; background: linear-gradient(90deg, #d9dbe0, #eceef1); }

  /* Business card front */
  .card-front { left: 577px; top: 74px; width: 267px; height: 153px; overflow: hidden; }
  .card-band { position: absolute; left: 0; top: 0; width: 18px; height: 100%; background: var(--brand-blue); }
  .card-front .brand { position: absolute; right: 11px; top: 18px; font-size: 14px; }
  .card-front .brand-square { width: 14px; height: 14px; }
  .card-name { position: absolute; right: 12px; top: 57px; text-align: right; line-height: 10px; }
  .card-name strong { display: block; font-size: 10px; color: var(--brand-blue); font-weight: 700; margin-bottom: 2px; }
  .card-name span { display: block; font-size: 7px; color: var(--text-grey); }
  .card-details { position: absolute; right: 12px; top: 86px; text-align: right; font-size: 6px; line-height: 8.3px; color: var(--text-grey); }
  .card-details .gap { height: 5px; }
  .card-front .slogan { position: absolute; left: 28px; bottom: 10px; font-size: 7px; }

  /* Business card back */
  .card-back { left: 877px; top: 143px; width: 267px; height: 153px; display: flex; align-items: center; justify-content: center; }
  .card-back .brand { color: var(--faint); font-size: 20px; }
  .card-back .brand-square { width: 22px; height: 22px; background: var(--faint); }

  /* Envelope back */
  .envelope-back { left: 615px; top: 350px; width: 549px; height: 248px; }
  .envelope-flap { position: absolute; left: 0; top: 0; width: 100%; height: 95px; }

  /* Envelope front */
  .envelope-front { left: 547px; top: 470px; width: 550px; height: 251px; }
  .envelope-front .brand { position: absolute; left: 0; top: 24px; font-size: 15px; }
  .envelope-front .brand-square { width: 34px; height: 34px; }
  .return-address { position: absolute; left: 38px; top: 68px; font-size: 8px; line-height: 10px; color: var(--text-grey); }
  .envelope-front .slogan { position: absolute; left: 38px; top: 92px; font-size: 7.5px; }
</style>
</head>
<body>

<section class="sheet letterhead">
  <div class="brand"><span class="brand-square"></span>CORBELL ESTATES LLC</div>
  <div class="slogan">Managing Homes, Building Community</div>
  <div class="letterhead-contact">
    2280 Harbor Ridge Drive #B210, Carlsbad, CA 92008<br>
    P: 760-555-0148 | F: 760-555-0192 | www.corbellestates.com
  </div>
  <div class="letter-body">
    <p class="greeting">Dear Mr. Hale,</p>
    <p>Lorem ipsum dolor sit amet, consectetur adipiscing elit. Donec orci purus, luctus vitae dignissim eu, iaculis sed purus. Vivamus faucibus, ipsum nec aliquet viverra, leo mauris condimentum ligula, sit amet sagittis enim ligula quis arcu. Nam egestas tortor id nisi porttitor mattis. In tortor ante, ultricies in suscipit a, tempus non massa. Vivamus et auctor mi. Fusce vel massa nulla. Phasellus nec eros mauris, et scelerisque orci.</p>
    <p>Donec malesuada orci vitae nulla accumsan porta a id massa. Quisque accumsan iaculis magna sit amet fringilla. Maecenas consequat, magna eget tincidunt semper, odio nibh rutrum mi, id feugiat ante nisi eu risus. Vestibulum nunc orci, rhoncus a placerat in, ultricies in mi. Cras mattis varius eros, vel fringilla nisi suscipit eget. Quisque scelerisque sagittis nulla at porttitor.</p>
    <p>Sed id augue vitae urna euismod commodo aliquet a quam. Pellentesque arcu velit, cursus et malesuada ut, consequat et diam. Nullam erat sem, rhoncus id ullamcorper vitae, rhoncus et arcu. In ultricies ultricies nulla, ut rutrum nisi iaculis at. Donec eu magna a metus ornare faucibus. Fusce aliquet faucibus ultricies. Morbi semper, est id tincidunt gravida, sem arcu adipiscing lacus, ac bibendum nulla leo eu purus. Quisque nec diam sed risus consectetur a ccumsan quis quis nibh. Vestibulum id purus lorem.</p>
    <p>It is a long established fact that a reader will be distracted by the readable content of a page when looking at its layout. The point of using Lorem Ipsum is that it has a more-or-less normal distribution of letters, as opposed to using 'Content here, content here', making it look like readable English. Many desktop publishing packages</p>
    <p class="closing">Sincerely,</p>
    <div class="signature" role="img" aria-label="Handwritten signature"></div>
  </div>
</section>

<section class="sheet card-front">
  <div class="card-band"></div>
  <div class="brand"><span class="brand-square"></span>CORBELL ESTATES LLC</div>
  <div class="card-name">
    <strong>DANA WHITFIELD</strong>
    <span>Property Manager</span>
  </div>
  <div class="card-details">
    2280 Harbor Ridge Drive #B210<br>
    Carlsbad, CA 92008
    <div class="gap"></div>
    Phone: 760-555-0148<br>
    Fax: 760-555-0192<br>
    dana@corbellestates.com<br>
    www.corbellestates.com
  </div>
  <div class="slogan">Managing Homes,<br>Building Community</div>
</section>

<section class="sheet card-back">
  <div class="brand"><span class="brand-square"></span>CORBELL ESTATES</div>
</section>

<section class="sheet envelope-back">
  <svg class="envelope-flap" viewBox="0 0 549 95" preserveAspectRatio="none" aria-hidden="true">
    <path d="M12 0 L30 78 Q33 91 48 91 L501 91 Q516 91 519 78 L537 0" fill="none" stroke="var(--line)" stroke-width="1"/>
  </svg>
</section>

<section class="sheet envelope-front">
  <div class="brand"><span class="brand-square"></span>CORBELL ESTATES LLC</div>
  <div class="return-address">
    2280 Harbor Ridge Drive #B210<br>
    Carlsbad, CA 92008
  </div>
  <div class="slogan">Managing Homes, Building Community</div>
</section>

</body>
</html>
```